Plastic Surgeon Needs a business card desing

I need a plastic surgeon business card, Im young , innovative , not afraid of thinking out of the box, What I dont like is human figures or scalpes as designing the card, because I think they are old fashion, I think my name is my strongest card, so I try to find the desing to be something elegant , simple , slick , stylish , radiant with carimsa!

Target Market(s)

PLastics Surgery Patients and doctors to have my data

Industry/Entity Type

Plastic

Contact Information for Business Card

phone numbers need to be legible , right now i have grey scales so they a not to legible

Font styles to use
Serif
Sans Serif

Requirements
Must have
• Personality, and it has to look like a doctor card, not a buisness man card, that is why i think it should be clean , clear , and legible
Nice to have
• Stylilsh, not to heavy card, in means of colors and logos, i think it should give a sensation of health
• Im not sure to have the logo of the hospital i work
Should not have
• human figures
• Hands
• Surgeons

```html
<!DOCTYPE html>
<html lang="es">
<head>
<meta charset="utf-8">
<title>Dr. Marco Velarde – Tarjeta de presentación</title>
<link href="https://fonts.googleapis.com/css2?family=Didact+Gothic&display=swap" rel="stylesheet">
<style>
  :root {
    --page-bg: #1a1a1d;
    --card-stock: #f4f2ee;
    --ink-light: #ffffff;
    --tone-magenta: #d2246f;
    --tone-violet: #7a3ea8;
    --tone-blue: #5a74c9;
    --tone-orange: #f07a3a;
    --tone-gold: #e6b33c;
  }
  html, body {
    margin: 0;
    width: 1200px;
    height: 797px;
    overflow: hidden;
    background: var(--page-bg);
  }
  .canvas {
    position: relative;
    width: 1200px;
    height: 797px;
    display: flex;
    align-items: center;
    justify-content: center;
  }
  .business-card {
    position: relative;
    width: 900px;
    height: 514px;
    background: var(--card-stock);
    box-sizing: border-box;
    padding: 24px;
  }
  .card-face {
    position: relative;
    width: 100%;
    height: 100%;
    overflow: hidden;
    font-family: "Didact Gothic", "Century Gothic", sans-serif;
    color: var(--ink-light);
  }
  .abstract-backdrop {
    position: absolute;
    inset: 0;
    background:
      radial-gradient(ellipse 18% 30% at 88% 30%, var(--tone-gold) 0%, transparent 70%),
      radial-gradient(ellipse 25% 45% at 12% 35%, var(--tone-orange) 0%, transparent 75%),
      radial-gradient(ellipse 30% 50% at 30% 20%, var(--tone-blue) 0%, transparent 75%),
      radial-gradient(ellipse 35% 55% at 70% 15%, var(--tone-violet) 0%, transparent 75%),
      linear-gradient(160deg, #9b3f9c 0%, var(--tone-magenta) 55%, #c8195f 100%);
    filter: saturate(1.1);
  }
  .card-content {
    position: absolute;
    left: 0;
    right: 0;
    top: 40px;
    text-align: center;
    padding-left: 60px;
  }
  .brand-mark {
    display: inline-flex;
    align-items: center;
    gap: 10px;
    font-size: 22px;
    letter-spacing: 2px;
    margin-bottom: 14px;
  }
  .brand-mark .dot {
    width: 14px;
    height: 14px;
    border-radius: 50%;
    background: var(--ink-light);
  }
  .doctor-name {
    margin: 0;
    font-weight: 400;
    font-size: 54px;
    letter-spacing: 1px;
    line-height: 1;
  }
  .specialty {
    display: inline-block;
    margin-top: 8px;
    font-size: 24px;
    border-bottom: 1.5px solid var(--ink-light);
    padding-bottom: 2px;
  }
  .contact {
    margin-top: 26px;
    font-size: 17px;
    line-height: 1.35;
    letter-spacing: 0.5px;
  }
  .contact .email { margin-bottom: 14px; }
  .contact .phones span + span { margin-left: 26px; }
</style>
</head>
<body>
  <main class="canvas">
    <article class="business-card">
      <div class="card-face">
        <div class="abstract-backdrop" role="img" aria-label="Fondo abstracto difuminado en tonos magenta, violeta, azul y naranja"></div>
        <div class="card-content">
          <div class="brand-mark"><span class="dot"></span><span>Velarde</span></div>
          <h1 class="doctor-name">DR. MARCO VELARDE</h1>
          <div class="specialty">cirugía plástica, estética y reconstructiva</div>
          <div class="contact">
            <div class="email">marco@drvelarde.com</div>
            <div class="phones"><span>Cel.33 2741 5068</span><span>Tel. 01 (03) 3612 7790</span></div>
            <div>Av. Colomos 2185, Int. 45</div>
            <div>Torre Médica Sol Poniente</div>
            <div>Guadalajara, Jalisco México</div>
          </div>
        </div>
      </div>
    </article>
  </main>
</body>
</html>
```